Business Card and Logo tweak for a Language Boarding School

we are a boadring langauge school for under 18 international student.
We call ourselves " HCSC" - Harwick Crossway Study Centre
We are one of the TQ "tidewater quarters" Melbourne campus for TQ high school preparation program.

our address is 14 Orrin Lane Brighton 3187
Ph: 03 95550142
Email: info@myhcsc-example.com
Website: www.myhcsc-example.com

We have our HCSC logo, but not very satisfied. May be you can tweak it furhter with the fond or formations.

Basically the business card list all relevant info on one side and list all our programs on the other side.

The program we have:
ELICOS with Boarding for U18 Students
HSP-High School Preparation Program
PSP- Primary School Preparation Program
Junior Holiday Program & Study Tours
After School Tutoring
Student Wellbeing and Counselling

```html
<!DOCTYPE html>
<html lang="en">
<head>
<meta charset="utf-8">
<title>HCSC Business Card</title>
<link href="https://fonts.googleapis.com/css2?family=Questrial&display=swap" rel="stylesheet">
<style>
  :root {
    --page-bg: #e6e7ea;
    --brand-blue: #1d4fa0;
    --brand-blue-deep: #173f86;
    --tint-blue: #3a5d9c;
    --tint-blue-soft: #5876ad;
    --photo-warm: #c9a27e;
    --photo-green: #7fa77a;
    --photo-teal: #5fae93;
    --ink-light: #ffffff;
    --accent-star: #f1e7b0;
  }
  * { margin: 0; padding: 0; box-sizing: border-box; }
  html, body {
    width: 1200px; height: 1200px; overflow: hidden;
    background: var(--page-bg);
    font-family: "Questrial", "Century Gothic", sans-serif;
    color: var(--ink-light);
  }
  .sheet {
    width: 1200px; height: 1200px;
    display: flex; flex-direction: column; align-items: center;
    justify-content: center; gap: 24px;
  }
  .card {
    position: relative; width: 960px; height: 549px; overflow: hidden;
    box-shadow: 0 6px 18px rgba(0,0,0,.18);
  }

  /* Front: contact side */
  .card--front { background: var(--brand-blue); }
  .card--front .photo-area {
    position: absolute; right: 0; bottom: 0; width: 70%; height: 100%;
    background: linear-gradient(135deg, var(--photo-green) 0%, var(--photo-warm) 45%, #e2c7a8 65%, var(--photo-teal) 100%);
    clip-path: ellipse(100% 100% at 100% 100%);
  }
  .brand {
    position: absolute; display: flex; align-items: center; gap: 14px;
  }
  .brand__dot {
    width: 44px; height: 44px; border: 4px solid var(--ink-light); border-radius: 50%;
  }
  .brand__name {
    font-size: 22px; line-height: 1.05; letter-spacing: 1px;
    text-transform: uppercase; width: 200px;
  }
  .card--front .brand { top: 40px; left: 48px; }
  .contact {
    position: absolute; top: 150px; left: 48px; list-style: none;
    font-size: 28px; line-height: 1.2;
  }
  .contact li { display: flex; align-items: flex-start; gap: 16px; margin-bottom: 14px; }
  .contact svg { flex: none; width: 34px; height: 34px; margin-top: 1px; }
  .website {
    position: absolute; left: 48px; bottom: 44px; font-size: 40px; letter-spacing: .5px;
  }

  /* Back: programs side */
  .card--back {
    background: linear-gradient(160deg, var(--tint-blue-soft) 0%, var(--tint-blue) 45%, var(--brand-blue-deep) 100%);
  }
  .card--back .photo-area {
    position: absolute; inset: 0;
    background: radial-gradient(ellipse at 75% 70%, rgba(120,150,200,.35), transparent 60%);
  }
  .card--back .brand { top: 52px; left: 340px; }
  .programs {
    position: absolute; top: 172px; left: 70px; font-size: 31px; line-height: 1.28;
  }
  .programs__title { margin-bottom: 4px; }
  .programs__list { list-style: none; }
  .programs__list li::before { content: "\2605"; font-size: 18px; margin-right: 12px; vertical-align: 4px; }
  .sparkle { position: absolute; top: 140px; right: 260px; color: var(--accent-star); font-size: 18px; }
</style>
</head>
<body>
<main class="sheet">
  <section class="card card--front">
    <div class="photo-area" role="img" aria-label="Photo of smiling international students together outdoors"></div>
    <div class="brand">
      <span class="brand__dot"></span>
      <span class="brand__name">Harwick Crossway Study Centre</span>
    </div>
    <ul class="contact">
      <li>
        <svg viewBox="0 0 34 34"><circle cx="17" cy="17" r="17" fill="#fff"/><rect x="9" y="11" width="16" height="12" rx="1.5" fill="none" stroke="#1d4fa0" stroke-width="2"/><path d="M9.5 12l7.5 6 7.5-6" fill="none" stroke="#1d4fa0" stroke-width="2"/></svg>
        info@myhcsc-example.com
      </li>
      <li>
        <svg viewBox="0 0 34 34"><circle cx="17" cy="17" r="17" fill="#fff"/><path d="M12 9c1 0 2 3 2.5 4s-1.5 2-1 3 3 4 4.5 4.5 2-1.5 3-1 4 1.5 4 2.5-2 3.5-4 3.5c-5 0-12-7-12-12 0-2 2.5-4.5 3-4.5z" fill="#1d4fa0"/></svg>
        03 95550142
      </li>
      <li>
        <svg viewBox="0 0 34 34"><circle cx="17" cy="17" r="17" fill="#fff"/><path d="M17 8a6 6 0 0 0-6 6c0 5 6 12 6 12s6-7 6-12a6 6 0 0 0-6-6z" fill="#1d4fa0"/><circle cx="17" cy="14" r="2.3" fill="#fff"/></svg>
        <span>14 Orrin Lane<br>Brighton 3187</span>
      </li>
    </ul>
    <p class="website">www.myhcsc-example.com</p>
  </section>

  <section class="card card--back">
    <div class="photo-area" role="img" aria-label="Blue-tinted photo of international students in the background"></div>
    <div class="brand">
      <span class="brand__dot"></span>
      <span class="brand__name">Harwick Crossway Study Centre</span>
    </div>
    <span class="sparkle">&#10023;</span>
    <div class="programs">
      <p class="programs__title">The program we have:</p>
      <ul class="programs__list">
        <li>ELICOS with Boarding for U18 Students</li>
        <li>HSP-High School Preparation Program</li>
        <li>PSP- Primary School Preparation Program</li>
        <li>Junior Holiday Program &amp; Study Tours</li>
        <li>After School Tutoring</li>
        <li>Student Wellbeing and Counselling</li>
      </ul>
    </div>
  </section>
</main>
</body>
</html>
```